This book will apply the 12 Steps to gaming addiction, also known as video game addiction. The primary purpose of the book is to provide an effective solution for this new type of addiction. The solution is based on the rich and successful concepts of traditional twelve-step programs like RL.

The title on the cover will be "Nine Doors Past the Glowing Screen" and "by Martin Quorby". A subtitle can be used if it works in your design of "A Practical Path Beyond Compulsive Console Play". Cover will be for a 6" x 9" book approximately 110 pages in length.

Some back cover text including some review quotes and an author bio are in the attached Word doc. There is also an author photo attached for for the back cover.

Requirements
Must have
• For the cover design it could be stylized, or an image, a partial image, or whatever. I am open to suggestions. Think about what would be noticed by a person searching for help with moderating their video game use, or by the parents or loved ones of problem gamers. Something contemporary and eye catching.

```html
<!DOCTYPE html>
<html lang="en">
<head>
<meta charset="utf-8">
<title>Nine Doors Past the Glowing Screen – Cover Wrap</title>
<link rel="stylesheet" href="https://fonts.googleapis.com/css2?family=Montserrat:wght@400;600;800;900&family=Great+Vibes&family=Open+Sans:ital,wght@0,400;0,700;1,400&display=swap">
<style>
  :root {
    --stage: #e9e9e9;
    --ink-dark: #0d0d0e;
    --ink-mid: #1b1b1d;
    --paper-text: #f2f2f2;
    --muted-text: #b9b9bb;
    --accent-red: #e0161d;
    --deep-red: #7a0509;
  }
  * { margin: 0; padding: 0; box-sizing: border-box; }
  html, body { width: 849px; height: 1200px; overflow: hidden; }
  body {
    background: var(--stage);
    display: flex; align-items: center; justify-content: center;
    font-family: "Open Sans", sans-serif;
  }
  .cover-wrap {
    width: 809px; height: 592px;
    display: flex;
    background: radial-gradient(ellipse at 70% 40%, var(--ink-mid), var(--ink-dark) 75%);
    box-shadow: 0 8px 24px rgba(0,0,0,.25);
    color: var(--paper-text);
  }
  /* Back cover */
  .back-cover {
    width: 397px; height: 100%;
    padding: 34px 32px 30px;
    display: flex; flex-direction: column;
  }
  .praise-heading {
    font-family: "Montserrat", sans-serif;
    font-weight: 800; font-size: 13px; line-height: 1.25;
    text-align: center; letter-spacing: .5px; margin-bottom: 16px;
  }
  .review { font-size: 7.6px; line-height: 1.5; margin-bottom: 11px; text-align: justify; }
  .review-source { display: block; color: var(--accent-red); font-weight: 700; font-style: italic; margin-top: 2px; }
  .author-block { margin-top: auto; display: flex; gap: 12px; align-items: center; }
  .author-photo {
    width: 72px; height: 86px; flex-shrink: 0;
    background: linear-gradient(160deg, #6c6c70, #2a2a2d);
  }
  .author-bio { font-size: 7.6px; line-height: 1.5; color: var(--muted-text); }
  .author-bio strong { color: var(--paper-text); }
  /* Spine */
  .spine {
    width: 20px; height: 100%;
    border-left: 1px solid #2a2a2c; border-right: 1px solid #2a2a2c;
    display: flex; align-items: center; justify-content: center;
  }
  .spine-text {
    writing-mode: vertical-rl;
    font-family: "Montserrat", sans-serif; font-size: 8px; font-weight: 800;
    letter-spacing: 1px; white-space: nowrap;
    display: flex; gap: 40px;
  }
  .spine-author { color: var(--muted-text); font-weight: 600; }
  /* Front cover */
  .front-cover {
    width: 392px; height: 100%;
    position: relative;
    display: flex; flex-direction: column; align-items: center;
    padding-top: 30px;
  }
  .front-author {
    font-family: "Montserrat", sans-serif; font-weight: 600;
    font-size: 10px; letter-spacing: 3px; color: var(--muted-text);
  }
  .title-block { margin-top: 30px; text-align: center; line-height: 1; }
  .title-lead { font-family: "Montserrat", sans-serif; font-weight: 600; font-size: 20px; }
  .title-main { font-family: "Montserrat", sans-serif; font-weight: 900; font-size: 46px; letter-spacing: -1px; }
  .title-script { font-family: "Great Vibes", cursive; color: var(--accent-red); font-size: 42px; margin: -2px 0 -6px; }
  .title-tail { font-family: "Montserrat", sans-serif; font-weight: 800; font-size: 26px; letter-spacing: .5px; }
  .controller-art {
    position: absolute; left: 0; right: 0; bottom: 0; height: 285px;
    background: radial-gradient(ellipse at 50% 55%, var(--accent-red) 0%, var(--deep-red) 45%, var(--ink-dark) 78%);
  }
</style>
</head>
<body>
  <main class="cover-wrap">
    <section class="back-cover">
      <h2 class="praise-heading">PRAISE FOR<br>NINE DOORS PAST THE GLOWING SCREEN</h2>
      <p class="review">“A clear, compassionate guide that turns proven recovery steps into daily habits. Families will find real hope here, and players will find a way back to balance.”<span class="review-source">– Dana Whitcombe, Licensed Family Counselor</span></p>
      <p class="review">“If you or someone you love cannot put the controller down, read this book. It speaks plainly and offers a path that works.”<span class="review-source">– Rafael Ostrin, Youth Pastor</span></p>
      <p class="review">“Honest, practical and never preachy. Each chapter gives readers a small step they can take today.”<span class="review-source">– Colette Marsh, School Psychologist</span></p>
      <p class="review">“An effective approach for a modern struggle. The author blends experience and research into something any reader can follow.”<span class="review-source">– Theo Brannick, Recovery Coach</span></p>
      <div class="author-block">
        <div class="author-photo" role="img" aria-label="Author portrait photograph"></div>
        <p class="author-bio"><strong>Martin Quorby</strong> is a technology consultant and writer with many years of experience helping families find healthier ways to live with screens. He shares the steps that changed his own life.</p>
      </div>
    </section>
    <section class="spine">
      <div class="spine-text">
        <span class="spine-author">MARTIN QUORBY</span>
        <span class="spine-title">NINE DOORS PAST THE GLOWING SCREEN</span>
      </div>
    </section>
    <section class="front-cover">
      <p class="front-author">MARTIN QUORBY</p>
      <h1 class="title-block">
        <span class="title-lead">Nine</span><br>
        <span class="title-main">DOORS</span><br>
        <span class="title-script">past the</span><br>
        <span class="title-tail">GLOWING SCREEN</span>
      </h1>
      <div class="controller-art" role="img" aria-label="Glossy red game controller on a dark background"></div>
    </section>
  </main>
</body>
</html>
```